eBook Cover Design Project - Midwinter Promises

We need an ebook cover design for our new digital only title for Lantern Press.

Lantern Press is Romance. Lantern will own Romance in digital-first as Bellweather owns Romance in print and ebook.

We are looking for FUN, MODERN, PREMIUM designs. Please keep the look clean and edgy but have fun with it; be flirty - it's romance!!!

Target Market(s)

30-55 year old women.

Industry/Entity Type

Digital

Requirements
Must have
• Must work as a black and white image as well as a colour image.
- Must be easily viewed at thumbnail size.
- Title must always be larger than the author name. Both must appear on cover.
- Final file should be a JPEG supplied at 2240 pixels (H) X 1400 pixels (W).
- See attached document for story report.
- If using people on the cover refer to character traits in story report.
Should not have
• Offensive or pornographic content.
- Too many elements – keep it simple.

```html
<!DOCTYPE html>
<html lang="en">
<head>
<meta charset="utf-8">
<title>Midwinter Promises — Maren Holloway</title>
<link rel="stylesheet" href="https://fonts.googleapis.com/css2?family=Pinyon+Script&family=Italianno&display=swap">
<style>
  :root {
    --paint-white: #fbf8ea;
    --paint-yellow: #f2d62a;
    --paint-gold: #e0a21c;
    --paint-orange: #d4661c;
    --shadow-brown: #4a3a1e;
    --gown-violet: #6b4ad6;
    --gown-deep: #3b2388;
    --gown-night: #24124f;
    --band-magenta: rgba(150, 22, 112, 0.86);
    --band-edge: rgba(120, 14, 88, 0.9);
    --title-white: #ffffff;
    --author-cream: #f5eca4;
  }

  * { margin: 0; padding: 0; box-sizing: border-box; }

  html, body {
    width: 750px;
    height: 1200px;
    overflow: hidden;
    background: #ffffff;
  }

  .cover {
    position: relative;
    width: 750px;
    height: 1200px;
    overflow: hidden;
  }

  .cover-artwork {
    position: absolute;
    inset: 0;
    background:
      radial-gradient(ellipse 60% 40% at 52% 30%, rgba(74, 58, 30, 0.55), transparent 70%),
      radial-gradient(ellipse 45% 38% at 70% 32%, rgba(107, 74, 214, 0.75), transparent 70%),
      linear-gradient(115deg, var(--paint-white) 0%, var(--paint-yellow) 22%, var(--paint-gold) 40%, var(--paint-orange) 52%, transparent 62%),
      linear-gradient(180deg, var(--paint-white) 0%, #f0d870 30%, var(--gown-violet) 58%, var(--gown-deep) 80%, var(--gown-night) 100%);
  }

  .title-band {
    position: absolute;
    left: 0;
    top: 690px;
    width: 750px;
    height: 270px;
    background: linear-gradient(180deg, var(--band-magenta), var(--band-edge));
  }

  .book-title {
    position: absolute;
    left: 0;
    top: 690px;
    width: 750px;
    height: 270px;
    text-align: center;
    font-family: "Pinyon Script", cursive;
    font-weight: 400;
    color: var(--title-white);
    line-height: 1;
  }

  .book-title .title-line-one {
    display: block;
    font-size: 86px;
    padding-top: 22px;
    letter-spacing: 1px;
  }

  .book-title .title-line-two {
    display: block;
    font-size: 128px;
    margin-top: -8px;
  }

  .author-name {
    position: absolute;
    left: 0;
    top: 995px;
    width: 750px;
    text-align: center;
    font-family: "Italianno", cursive;
    font-size: 40px;
    color: var(--author-cream);
    text-shadow: 1px 1px 2px #1a0c2e;
  }
</style>
</head>
<body>
  <main class="cover">
    <div class="cover-artwork" role="img" aria-label="Painted romance illustration: a dark-haired woman in a flowing violet off-shoulder gown embraced by a bare-chested man, set against sweeping yellow and orange brushstrokes, the gown's skirt filling the lower cover"></div>
    <div class="title-band"></div>
    <h1 class="book-title">
      <span class="title-line-one">Midwinter</span>
      <span class="title-line-two">Promises</span>
    </h1>
    <p class="author-name">Maren Holloway</p>
  </main>
</body>
</html>
```